Quibont homepage

Re-design www.quibont-example.com. Visitors are developers and CTOs. Something simple and straightforward. Need different and special landingpage.
I like this page: http://melvantry-example.io/ (service is also similar).
Logo is at http://www.quibont-example.com/quibont.svg
Be bold with content you see on www.quibont-example.com.
If you want ... make main message shorter, add links that doesn't exist, remove something etc.
Landing page should be cleaner than it is now.
Things what I want to have on page (missing on quibont-example.com):
- testimonials
- contact form (can be simple as "send us e-mail...")
Quibont supports Tavix, Brimhollow, Fenlow and Korvet. You are welcome to use logos for those databases.
CTO-s and developers/programmers
It Service

```html
<!DOCTYPE html>
<html lang="en">
<head>
<meta charset="utf-8">
<title>Quibont — Boost Up Your Creation</title>
<link href="https://fonts.googleapis.com/css2?family=Roboto:wght@300;400;500&display=swap" rel="stylesheet">
<style>
  :root {
    --teal: #1aa7c3;
    --teal-hero: #1a97b0;
    --teal-deep: #0f7d94;
    --teal-button: #17677a;
    --nav-active: #1e9fbf;
    --ink: #333a3d;
    --nav-ink: #444b4e;
    --white: #ffffff;
  }
  * { box-sizing: border-box; margin: 0; padding: 0; }
  html, body { width: 1200px; height: 940px; overflow: hidden; background: var(--white); }
  body { font-family: "Roboto", Arial, sans-serif; color: var(--ink); position: relative; }

  .site-header { height: 83px; position: relative; background: var(--white); }
  .brand { position: absolute; left: 68px; top: 27px; display: flex; align-items: center; gap: 8px; }
  .brand-square { width: 22px; height: 22px; background: var(--teal); }
  .brand-name { font-size: 24px; font-weight: 400; color: var(--ink); letter-spacing: .5px; }
  .main-nav { position: absolute; right: 59px; top: 32px; display: flex; gap: 27px; }
  .main-nav a { font-size: 16px; color: var(--nav-ink); text-decoration: none; }
  .main-nav a.is-active { color: var(--nav-active); }

  .hero { position: absolute; top: 83px; left: 0; width: 1200px; height: 564px; overflow: hidden; }
  .hero-backdrop { position: absolute; inset: 0;
    background:
      linear-gradient(155deg, rgba(8,110,135,.55) 0%, rgba(8,110,135,0) 45%),
      linear-gradient(180deg, var(--teal-deep) 0%, var(--teal-hero) 50%, var(--teal) 100%); }
  .hero-content { position: relative; text-align: center; color: var(--white); }
  .hero-mark { width: 60px; height: 60px; border-radius: 50%; background: rgba(255,255,255,.35); margin: 125px auto 0; }
  .hero-title { font-size: 36px; font-weight: 500; margin-top: 12px; line-height: 1.2; }
  .hero-lead { font-size: 24px; font-weight: 300; line-height: 33px; margin: 34px auto 0; width: 760px; }
  .hero-lead strong { font-weight: 400; }
  .get-button { display: inline-flex; align-items: center; gap: 26px; margin-top: 35px;
    height: 51px; padding: 0 30px 0 43px; border-radius: 26px; background: var(--teal-button);
    border: 1px solid rgba(255,255,255,.15); color: var(--white); font-size: 24px; font-weight: 400; text-decoration: none; }
  .platform-dots { display: flex; gap: 12px; }
  .platform-dots span { width: 16px; height: 16px; border-radius: 50%; background: rgba(255,255,255,.7); }

  .features { position: absolute; top: 647px; left: 0; width: 1200px; }
  .features-title { text-align: center; font-size: 26px; font-weight: 400; margin-top: 78px; }
  .feature-list { list-style: none; position: relative; height: 120px; margin-top: 62px; }
  .feature { position: absolute; width: 140px; margin-left: -70px; text-align: center; }
  .feature-icon { width: 82px; height: 82px; border-radius: 50%; background: var(--teal); margin: 0 auto; overflow: hidden; position: relative; }
  .feature-icon svg { position: absolute; inset: 0; }
  .feature-label { display: block; font-size: 15px; margin-top: 12px; color: var(--ink); }
</style>
</head>
<body>
  <header class="site-header">
    <a class="brand" href="#"><span class="brand-square"></span><span class="brand-name">Quibont</span></a>
    <nav class="main-nav">
      <a href="#">About</a>
      <a href="#" class="is-active">Installation</a>
      <a href="#">Documentation</a>
      <a href="#">Benefits</a>
      <a href="#">Compare</a>
      <a href="#">Download</a>
    </nav>
  </header>

  <section class="hero">
    <div class="hero-backdrop" role="img" aria-label="Blurred photo of a laptop on a desk tinted in teal"></div>
    <div class="hero-content">
      <div class="hero-mark"></div>
      <h1 class="hero-title">Boost Up Your Creation</h1>
      <p class="hero-lead"><strong>Quibont</strong> speed up building mobile apps, JavaScript heavy interfaces and integrations by reducing amount of code and todo list.</p>
      <a class="get-button" href="#">Get Quibont <span class="platform-dots"><span></span><span></span><span></span></span></a>
    </div>
  </section>

  <section class="features">
    <h2 class="features-title">What can you do with Quibont</h2>
    <ul class="feature-list">
      <li class="feature" style="left:155px">
        <div class="feature-icon"><svg width="82" height="82" viewBox="0 0 82 82">
          <path d="M23 50 L23 60 L60 82 L82 82 L82 45 L59 24Z" fill="rgba(0,0,0,.12)"/>
          <rect x="23" y="25" width="36" height="25" rx="2" fill="none" stroke="#fff" stroke-width="4"/>
          <rect x="37" y="50" width="8" height="6" fill="#fff"/><rect x="31" y="56" width="20" height="3" fill="#fff"/></svg></div>
        <span class="feature-label">Desktop</span></li>
      <li class="feature" style="left:333px">
        <div class="feature-icon"><svg width="82" height="82" viewBox="0 0 82 82">
          <path d="M30 58 L55 82 L82 82 L82 55 L52 24Z" fill="rgba(0,0,0,.12)"/>
          <rect x="30" y="22" width="22" height="38" rx="3" fill="none" stroke="#fff" stroke-width="3.5"/>
          <circle cx="41" cy="54" r="2" fill="#fff"/></svg></div>
        <span class="feature-label">Mobiles</span></li>
      <li class="feature" style="left:511px">
        <div class="feature-icon"><svg width="82" height="82" viewBox="0 0 82 82">
          <path d="M26 56 L50 82 L82 82 L82 52 L56 25Z" fill="rgba(0,0,0,.12)"/>
          <polyline points="27,55 36,40 44,48 55,27" fill="none" stroke="#fff" stroke-width="3"/>
          <g fill="#fff"><circle cx="27" cy="55" r="3.5"/><circle cx="36" cy="40" r="3.5"/><circle cx="44" cy="48" r="3.5"/><circle cx="55" cy="27" r="3.5"/></g></svg></div>
        <span class="feature-label">Analyses</span></li>
      <li class="feature" style="left:687px">
        <div class="feature-icon"><svg width="82" height="82" viewBox="0 0 82 82">
          <path d="M28 52 L55 82 L82 82 L82 55 L57 32Z" fill="rgba(0,0,0,.12)"/>
          <text x="41" y="52" text-anchor="middle" font-family="Roboto, Arial, sans-serif" font-size="28" font-weight="500" fill="#fff">JS</text></svg></div>
        <span class="feature-label">Javascript</span></li>
      <li class="feature" style="left:868px">
        <div class="feature-icon"><svg width="82" height="82" viewBox="0 0 82 82">
          <path d="M24 50 L52 82 L82 82 L82 52 L58 30Z" fill="rgba(0,0,0,.12)"/>
          <path d="M41 22 L58 30 L41 38 L24 30Z" fill="#fff"/>
          <path d="M24 33 L39 40 L39 60 L24 52Z" fill="#fff"/>
          <path d="M58 33 L43 40 L43 60 L58 52Z" fill="#fff"/></svg></div>
        <span class="feature-label">API for JS</span></li>
      <li class="feature" style="left:1046px">
        <div class="feature-icon"><svg width="82" height="82" viewBox="0 0 82 82">
          <path d="M23 55 L50 82 L82 82 L82 52 L59 27Z" fill="rgba(0,0,0,.12)"/>
          <rect x="23" y="27" width="36" height="28" fill="none" stroke="#fff" stroke-width="3.5"/>
          <rect x="23" y="27" width="36" height="6" fill="#fff"/>
          <rect x="29" y="38" width="9" height="12" fill="none" stroke="#fff" stroke-width="2.5"/>
          <rect x="41" y="38" width="12" height="12" fill="#fff"/></svg></div>
        <span class="feature-label">Websites</span></li>
    </ul>
  </section>
</body>
</html>
```